Flyer Design Size Qumbro Electrical pty ltd

Qumbro Electrical pty ltd (pty ltd )
we do all electrical work ,SAFTEY CHECKS,FIRE ALARMS,LIGHTING
,DATA &
COMMUNICATION
1 , we always look for safety fist
2. let license electrician do you job
3.Commercial
Industrial
residential
what e do ... lighting, power, data and communication, safety switches, upgrade switchbored,
change your old lights to LED down light energy safer and brighter
www.qumbroelectrical-example.com.au
qumbroelectrical@mailbox-example.com
mob, 0455 806 314
0468 230 571
up to 40% off
colors orange and black and white

```html
<!DOCTYPE html>
<html lang="en">
<head>
<meta charset="utf-8">
<title>Qumbro Electrical – Flyer</title>
<link rel="stylesheet" href="https://fonts.googleapis.com/css2?family=Arimo:wght@400;700&family=Kaushan+Script&display=swap">
<style>
  :root{
    --orange:#f26522;
    --charcoal:#262626;
    --charcoal-2:#3a3a3a;
    --grey-dark:#6e6e6e;
    --grey-mid:#a9a9a9;
    --grey-light:#d9d9d9;
    --white:#ffffff;
    --black:#111111;
    --page:#eceff1;
  }
  *{box-sizing:border-box;margin:0;padding:0}
  html,body{width:1200px;height:1077px;overflow:hidden}
  body{background:var(--page);font-family:"Arimo",Arial,sans-serif;position:relative}

  .flyer{position:absolute;width:560px;height:410px;overflow:hidden;
    box-shadow:0 6px 18px rgba(0,0,0,.25)}
  .flyer--front{left:40px;top:70px;background:radial-gradient(ellipse at 45% 60%,var(--grey-light) 0%,var(--grey-mid) 55%,var(--grey-dark) 100%)}
  .flyer--back{left:600px;top:590px;background:var(--white)}

  .top-stripe{position:absolute;left:0;top:0;width:100%;height:24px;background:var(--orange)}
  .header{position:absolute;left:0;top:24px;width:100%;height:126px;
    background:linear-gradient(180deg,var(--charcoal-2) 0%,var(--charcoal) 100%)}
  .brand{position:absolute;left:34px;top:44px;display:flex;align-items:center;gap:14px}
  .brand__mark{width:34px;height:34px;border:2px solid var(--white);border-radius:50%}
  .brand__name{color:var(--white);font-weight:700;font-size:28px;letter-spacing:.5px}

  .service{position:absolute;right:34px;top:18px;width:150px;text-align:center}
  .service__hours{color:var(--orange);font-weight:700;font-size:54px;line-height:1;letter-spacing:-1px}
  .service__label{margin-top:4px;background:linear-gradient(180deg,#8a8a8a,#5a5a5a);color:var(--white);
    font-size:19px;letter-spacing:3px;border-radius:8px 0 8px 0;padding:2px 0}

  .sectors{position:absolute;left:0;top:150px;width:100%;height:44px;background:var(--charcoal);
    border-top:3px solid var(--grey-mid);border-bottom:3px solid var(--grey-mid);
    display:flex;justify-content:center;align-items:center;gap:12px;
    color:var(--orange);font-weight:700;font-size:25px}
  .sectors__dot{width:9px;height:9px;border-radius:50%;background:var(--grey-mid)}

  .tagline{position:absolute;left:0;top:204px;width:100%;text-align:center;
    font-family:"Kaushan Script",cursive;font-size:25px;color:var(--black)}
  .services{position:absolute;left:34px;top:254px;list-style:none}
  .services li{color:var(--white);font-weight:700;font-size:17px;line-height:21px;
    text-shadow:0 1px 2px rgba(0,0,0,.5);display:flex;align-items:center;gap:8px}
  .services li::before{content:"";width:7px;height:7px;border-radius:50%;background:var(--orange)}

  .collage{position:absolute;left:330px;top:240px;width:210px;height:160px}
  .tile{position:absolute;border:5px solid var(--black);background:linear-gradient(135deg,#f4f4f4,#cfcfcf)}
  .tile--orange{border-color:var(--orange)}
  .tile--a{left:0;top:10px;width:90px;height:70px}
  .tile--b{left:120px;top:0;width:70px;height:65px}
  .tile--c{left:130px;top:90px;width:75px;height:65px}
  .tile--d{left:40px;top:55px;width:90px;height:95px;background:linear-gradient(135deg,#d8423a,#8e1d1a);border-color:#3a3a3a}

  .offer{position:absolute;left:0;top:210px;width:100%;text-align:center;
    font-weight:700;font-size:58px;color:var(--black);letter-spacing:-.5px}
  .offer__figure{color:var(--orange)}
  .partners{position:absolute;left:30px;top:290px;width:500px;display:flex;flex-wrap:wrap;gap:8px 10px}
  .partner{height:22px;border-radius:2px}
  .contact{position:absolute;left:30px;top:358px;right:20px;font-size:13px;color:var(--black);line-height:18px}
  .contact__label{color:var(--orange)}
  .contact__row{display:flex;gap:18px}
</style>
</head>
<body>

<section class="flyer flyer--front">
  <div class="top-stripe"></div>
  <header class="header">
    <div class="brand"><span class="brand__mark"></span><span class="brand__name">Qumbro Electrical</span></div>
    <div class="service"><div class="service__hours">24/7</div><div class="service__label">Service</div></div>
  </header>
  <div class="sectors"><span>Commercial</span><span class="sectors__dot"></span><span>Industrial</span><span class="sectors__dot"></span><span>Residential</span></div>
  <p class="tagline">We do all Electrical work</p>
  <ul class="services">
    <li>Data</li><li>Lighting</li><li>Fire Alarms</li><li>Safety Checks</li><li>Communication</li><li>Switchboard Upgrade</li>
  </ul>
  <div class="collage">
    <div class="tile tile--a tile--orange" role="img" aria-label="Photo of a switchboard"></div>
    <div class="tile tile--b" role="img" aria-label="Photo of a safety checklist"></div>
    <div class="tile tile--c tile--orange" role="img" aria-label="Photo of an LED downlight"></div>
    <div class="tile tile--d" role="img" aria-label="Photo of a fire alarm bell"></div>
  </div>
</section>

<section class="flyer flyer--back">
  <div class="top-stripe"></div>
  <header class="header">
    <div class="brand"><span class="brand__mark"></span><span class="brand__name">Qumbro Electrical</span></div>
    <div class="service"><div class="service__hours">24/7</div><div class="service__label">Service</div></div>
  </header>
  <div class="sectors"><span>Commercial</span><span class="sectors__dot"></span><span>Industrial</span><span class="sectors__dot"></span><span>Residential</span></div>
  <p class="offer">Up to <span class="offer__figure">40%</span> off</p>
  <div class="partners">
    <span class="partner" style="width:46px;background:#2a4a9a"></span>
    <span class="partner" style="width:36px;background:#4a6cb0"></span>
    <span class="partner" style="width:40px;background:#c33"></span>
    <span class="partner" style="width:62px;background:#2f8a3a"></span>
    <span class="partner" style="width:52px;background:#2d8ac9"></span>
    <span class="partner" style="width:48px;background:#d22"></span>
    <span class="partner" style="width:48px;background:#6aa52a"></span>
    <span class="partner" style="width:40px;background:#222"></span>
    <span class="partner" style="width:58px;background:#c32025"></span>
    <span class="partner" style="width:44px;background:#2a5fa8"></span>
    <span class="partner" style="width:52px;background:#3a3a3a"></span>
    <span class="partner" style="width:52px;background:#1d5fb0"></span>
    <span class="partner" style="width:44px;background:#d33"></span>
    <span class="partner" style="width:62px;background:#1a47a0"></span>
    <span class="partner" style="width:34px;background:#c22"></span>
    <span class="partner" style="width:52px;background:#e03a2f"></span>
  </div>
  <div class="contact">
    <div class="contact__row"><span><span class="contact__label">Tel: </span>0455 806 314 &nbsp; 0468 230 571</span></div>
    <div class="contact__row"><span><span class="contact__label">Email: </span>qumbroelectrical@mailbox-example.com</span></div>
    <div class="contact__row"><span><span class="contact__label">Web: </span>www.qumbroelectrical-example.com.au</span></div>
  </div>
</section>

</body>
</html>
```